Business Card Design Project

I have attached the logo and the colour pallete for the branding for the company.

Creative designs for business cards are needed.

The Company is modern corporate.

Industry/Entity Type

Business

```html
<!DOCTYPE html>
<html lang="en">
<head>
<meta charset="utf-8">
<title>Routewise Business Cards</title>
<link rel="stylesheet" href="https://fonts.googleapis.com/css2?family=Barlow:wght@400;500;600;700&display=swap">
<style>
  :root {
    --stage: #1e1e1e;
    --card-dark: #2b2b2b;
    --card-dark-deep: #1f1f1f;
    --paper: #ffffff;
    --ink: #231f20;
    --accent: #f26a1b;
    --accent-warm: #f7931e;
    --text-light: #f2f2f2;
  }
  * { box-sizing: border-box; margin: 0; padding: 0; }
  html, body {
    width: 1200px; height: 900px; overflow: hidden;
    background: var(--stage);
    font-family: "Barlow", sans-serif;
  }
  .card-set {
    position: relative; width: 1200px; height: 900px;
  }
  .card {
    position: absolute; top: 310px;
    width: 500px; height: 290px;
    border-radius: 28px; overflow: hidden;
    box-shadow: 0 18px 40px rgba(0,0,0,.55);
  }
  /* Back side */
  .card-back {
    left: 70px;
    background: linear-gradient(160deg, var(--card-dark) 0%, var(--card-dark-deep) 100%);
    display: flex; align-items: center; justify-content: center;
  }
  .brand {
    display: flex; align-items: center; gap: 14px;
    font-weight: 700; letter-spacing: -1px; line-height: 1;
  }
  .brand-dot {
    width: 18px; height: 18px; border-radius: 50%;
    background: var(--accent);
  }
  .card-back .brand { font-size: 70px; color: var(--paper); }
  /* Front side */
  .card-front { left: 630px; background: var(--card-dark); }
  .front-header {
    height: 150px; background: var(--paper);
    display: flex; align-items: center; padding-left: 40px;
  }
  .card-front .brand { font-size: 64px; color: var(--ink); }
  .accent-band {
    position: relative; height: 12px;
    background: linear-gradient(90deg, var(--accent), var(--accent-warm));
  }
  .accent-band::after {
    content: ""; position: absolute; left: 34px; top: 12px;
    border-left: 10px solid transparent; border-right: 0 solid transparent;
    border-top: 12px solid var(--accent);
  }
  .front-details {
    position: relative; height: 128px;
    padding: 14px 26px 0 26px; color: var(--text-light);
  }
  .person-name {
    color: var(--accent); font-weight: 600; font-size: 17px; line-height: 1.1;
  }
  .person-title { font-size: 12px; margin-top: 3px; }
  .address {
    position: absolute; left: 26px; top: 74px;
    font-size: 12.5px; line-height: 1.35;
  }
  .contact-list {
    position: absolute; right: 26px; top: 58px;
    list-style: none; font-size: 13px; line-height: 1.3;
  }
  .contact-label { color: var(--accent); font-weight: 500; }
</style>
</head>
<body>
  <main class="card-set">
    <section class="card card-back" aria-label="Card back">
      <div class="brand"><span>Routewise</span><span class="brand-dot"></span></div>
    </section>

    <section class="card card-front" aria-label="Card front">
      <header class="front-header">
        <div class="brand"><span>Routewise</span><span class="brand-dot"></span></div>
      </header>
      <div class="accent-band"></div>
      <div class="front-details">
        <p class="person-name">Daniel Harmon</p>
        <p class="person-title">Vice President</p>
        <address class="address" style="font-style:normal">
          48 Harbor Lane, Suite 210<br>Easton, 4410221
        </address>
        <ul class="contact-list">
          <li><span class="contact-label">Toll Free:</span> 555-010-204</li>
          <li><span class="contact-label">Cell:</span> 555-010-2088</li>
          <li><span class="contact-label">Email:</span> info@routewise.com</li>
          <li><span class="contact-label">Web:</span> www.routewise.com</li>
        </ul>
      </div>
    </section>
  </main>
</body>
</html>
```